Brambleton Business Card

I have a current card that I like it just needs a couple little changes to make it perfect. I would like the font size bigger so it could be easily read by older customers.

Business

```html
<!DOCTYPE html>
<html lang="en">
<head>
<meta charset="utf-8">
<title>Brambleton Motorsports and Marine – Business Card</title>
<link rel="stylesheet" href="https://fonts.googleapis.com/css2?family=Mako&family=Open+Sans:wght@400;600;700&family=Quicksand:wght@300;500&display=swap">
<style>
  :root {
    --backdrop: #6c6c6c;
    --card-front-deep: #0f1512;
    --card-front-mid: #173826;
    --card-back-light: #c9d0d2;
    --card-back-edge: #a9b1b4;
    --accent-green: #cfe98b;
    --accent-lime: #c3df6f;
    --text-light: #ffffff;
    --text-dark: #161616;
  }
  * { box-sizing: border-box; margin: 0; padding: 0; }
  html, body {
    width: 1200px;
    height: 1000px;
    overflow: hidden;
    background: var(--backdrop);
  }
  .card {
    position: absolute;
    box-shadow: 0 3px 10px rgba(0,0,0,0.45);
  }

  /* Front */
  .card--front {
    left: 261px; top: 81px;
    width: 681px; height: 388px;
    background:
      radial-gradient(ellipse 300px 220px at 180px 150px, rgba(63,174,92,0.45), transparent 70%),
      linear-gradient(180deg, var(--card-front-mid) 0%, #14251b 55%, var(--card-front-deep) 100%);
    color: var(--text-light);
    font-family: "Mako", sans-serif;
  }
  .emblem-area {
    position: absolute;
    left: 20px; top: 50px;
    width: 320px; height: 300px;
    border-radius: 50%;
    background: radial-gradient(circle at 45% 40%, rgba(120,220,140,0.35), rgba(63,174,92,0.08) 60%, transparent 75%);
  }
  .front-line {
    position: absolute;
    right: 24px;
    text-align: right;
    white-space: nowrap;
    line-height: 1.2;
  }
  .holder-name {
    top: 34px;
    font-family: "Quicksand", sans-serif;
    font-weight: 500;
    font-size: 31px;
    color: var(--accent-green);
  }
  .business-name {
    top: 88px;
    font-size: 58px;
    line-height: 1;
    color: var(--text-light);
  }
  .business-line {
    top: 150px;
    font-family: "Open Sans", sans-serif;
    font-weight: 700;
    font-size: 22px;
    color: var(--accent-lime);
  }
  .tagline {
    top: 184px;
    font-family: "Quicksand", sans-serif;
    font-weight: 300;
    font-size: 32px;
    color: var(--text-light);
  }
  .contact { font-size: 19px; }
  .contact--web { top: 232px; color: var(--accent-lime); }
  .contact--mail { top: 258px; }
  .contact--phone { top: 284px; }
  .contact--street { top: 310px; }
  .contact--city { top: 336px; }
  .label { color: var(--accent-lime); }

  /* Back */
  .card--back {
    left: 259px; top: 521px;
    width: 683px; height: 391px;
    background: radial-gradient(ellipse 420px 260px at 55% 45%, var(--card-back-light), var(--card-back-edge));
    color: var(--text-dark);
    text-align: center;
  }
  .services {
    position: absolute;
    left: 0; right: 0; top: 150px;
    font-family: "Mako", sans-serif;
  }
  .services__main {
    font-size: 26px;
    line-height: 36px;
    -webkit-text-stroke: 0.5px var(--text-dark);
  }
  .services__extra {
    margin-top: 6px;
    font-family: "Open Sans", sans-serif;
    font-weight: 600;
    font-size: 18px;
  }
  .hours {
    position: absolute;
    left: 0; right: 0; top: 358px;
    font-family: "Open Sans", sans-serif;
    font-size: 15.5px;
    letter-spacing: -0.1px;
    white-space: nowrap;
  }
</style>
</head>
<body>
  <section class="card card--front">
    <div class="emblem-area" role="img" aria-label="Brambleton emblem area with green light glow"></div>
    <p class="front-line holder-name">Dan Halvorsen</p>
    <p class="front-line business-name">Brambleton</p>
    <p class="front-line business-line">Motorsports and Marine</p>
    <p class="front-line tagline">Fun for all seasons!</p>
    <p class="front-line contact contact--web">www.brambletonmotorsports.com</p>
    <p class="front-line contact contact--mail">dan@brambletonmotorsports.com</p>
    <p class="front-line contact contact--phone"><span class="label">P:</span> 651-555-0142&nbsp; <span class="label">F:</span> 651-555-0187</p>
    <p class="front-line contact contact--street">2480 Birch Hollow Road</p>
    <p class="front-line contact contact--city">Lakeview, MN 55099</p>
  </section>

  <section class="card card--back">
    <div class="services">
      <p class="services__main">Servicing all makes &amp; models of boats,<br>snowmobiles, motorcycles and ATV’s.</p>
      <p class="services__extra">Custom welding available for aluminium and steel.</p>
    </div>
    <p class="hours">Hours: Mon - Wed 9am - 5:30pm • Thurs: 9am - 7pm • Fri: 9am - 5:30pm • Sat: 9am - 3:30pm</p>
  </section>
</body>
</html>
```